Business Card Design

Need a card designed to fit the tax preparation and accounting profession. Would like to include the following on side two of the card:

Tax Preparation and Audit Representation for:
Individuals
Partnerships
Corporations
Estates
Trusts
Other entities with tax reporting requirements

Industry/Entity Type

Accounting

Contact Information for Business Card

Whitcombe & Associates
Tax and Business Services
Gerald R Whitcombe III, EA, MS
Enrolled Agent P08637519
4172 Marrowind Lane, Suite D
Citrus Heights, CA 95621
(916) 482-6157
Email: ledgerpro729@mailbrook.example
www.ledgerhelpdesk.example

```html
<!DOCTYPE html>
<html lang="en">
<head>
<meta charset="utf-8">
<title>Whitcombe &amp; Associates — Business Card</title>
<link rel="stylesheet" href="https://fonts.googleapis.com/css2?family=Source+Sans+3:wght@400&display=swap">
<style>
  :root {
    --card-center: #3a3a3b;
    --card-mid: #262627;
    --card-edge: #161617;
    --accent-blue: #29a3d8;
    --text-white: #ffffff;
  }
  html, body {
    margin: 0;
    padding: 0;
    width: 1200px;
    height: 668px;
    overflow: hidden;
    background: var(--card-edge);
  }
  .card {
    position: relative;
    width: 1200px;
    height: 668px;
    overflow: hidden;
    background: radial-gradient(ellipse 70% 75% at 50% 42%, var(--card-center) 0%, var(--card-mid) 55%, var(--card-edge) 100%);
    font-family: "Source Sans 3", "Myriad Pro", Arial, sans-serif;
    color: var(--text-white);
  }
  .accent-bar {
    position: absolute;
    top: 184px;
    width: 22px;
    height: 302px;
    background: var(--accent-blue);
  }
  .accent-bar--left { left: 0; }
  .accent-bar--right { right: 0; }
  .firm-name {
    position: absolute;
    left: 198px;
    top: 250px;
    margin: 0;
    font-size: 88px;
    font-weight: 400;
    line-height: 88px;
    white-space: nowrap;
    letter-spacing: 0;
  }
  .firm-tagline {
    position: absolute;
    left: 255px;
    top: 340px;
    margin: 0;
    font-size: 41px;
    font-weight: 400;
    line-height: 41px;
    white-space: nowrap;
  }
</style>
</head>
<body>
  <main class="card">
    <div class="accent-bar accent-bar--left"></div>
    <div class="accent-bar accent-bar--right"></div>
    <h1 class="firm-name">Whitcombe &amp; Associates</h1>
    <p class="firm-tagline">Tax And Business Services</p>
  </main>
</body>
</html>
```